Business Card - Harlow Birch

Need Business Card design for company named Harlow Birch. Software development focused mainly on Ardel eKallo & oBix Apps. I've attached our logo with both a black and white background. Please add trademark symbol to logo when using.

```html
<!DOCTYPE html>
<html lang="en">
<head>
<meta charset="utf-8">
<title>Harlow Birch — Business Card</title>
<link href="https://fonts.googleapis.com/css2?family=Exo+2:wght@600&family=Ubuntu+Mono&display=swap" rel="stylesheet">
<style>
  :root {
    --backdrop: #d9d6d2;
    --card: #2a2a2a;
    --white: #f2f2f2;
    --dim: #5a5a5a;
    --faint: #444444;
    --yellow: #f2c21b;
    --orange: #f08a24;
    --red: #e2332a;
  }
  html, body {
    margin: 0;
    width: 1200px;
    height: 900px;
    overflow: hidden;
    background: var(--backdrop);
  }
  .sheet {
    width: 1200px;
    height: 900px;
    display: flex;
    flex-direction: column;
    align-items: center;
    justify-content: center;
    gap: 60px;
  }
  .card {
    position: relative;
    width: 525px;
    height: 300px;
    background: var(--card);
    box-shadow: 0 6px 18px rgba(0,0,0,0.25);
    overflow: hidden;
  }
  .card-front {
    display: flex;
    align-items: center;
    justify-content: center;
  }
  .brand {
    display: flex;
    align-items: center;
    gap: 14px;
  }
  .brand-mark {
    width: 22px;
    height: 22px;
    background: var(--orange);
  }
  .brand-name {
    font-family: "Exo 2", sans-serif;
    font-weight: 600;
    font-size: 40px;
    color: var(--white);
    letter-spacing: -0.5px;
  }
  .code {
    position: absolute;
    left: 30px;
    top: 30px;
    font-family: "Ubuntu Mono", monospace;
    font-size: 14px;
    line-height: 16px;
    color: var(--white);
    margin: 0;
    white-space: pre;
  }
  .code .ln { color: var(--faint); display: inline-block; width: 28px; }
  .code .var { color: var(--orange); }
  .code .key, .code .punct { color: var(--dim); }
  .code .www { color: var(--yellow); }
  .code .host { color: var(--orange); }
  .code .tld { color: var(--red); }
  .card-back .brand {
    position: absolute;
    right: 40px;
    bottom: 30px;
  }
  .card-back .brand-name { font-size: 30px; }
  .edge-rule {
    position: absolute;
    right: 16px;
    top: 20px;
    bottom: 20px;
    border-right: 1px dashed var(--faint);
  }
</style>
</head>
<body>
<main class="sheet">
  <section class="card card-front" aria-label="Card front">
    <div class="brand">
      <span class="brand-mark"></span>
      <span class="brand-name">Harlow Birch</span>
    </div>
  </section>

  <section class="card card-back" aria-label="Card back">
<pre class="code"><span class="ln">1</span><span class="var">hb</span> = {
<span class="ln">2</span>    <span class="key">"name"</span><span class="punct">    : "</span>Marcus Ellery<span class="punct">",</span>
<span class="ln">3</span>    <span class="key">"email"</span><span class="punct">   : "</span>info@harlowbirch.com<span class="punct">",</span>
<span class="ln">4</span>    <span class="key">"mobile"</span><span class="punct">  : "</span>555-014-2290<span class="punct">",</span>
<span class="ln">5</span>    <span class="key">"fax"</span><span class="punct">     : "</span>555-014-7731<span class="punct">",</span>
<span class="ln">6</span>    <span class="key">"url"</span><span class="punct">     : "</span>http://<span class="www">www.</span><span class="host">harlowbirch</span><span class="tld">.com</span><span class="punct">",</span>
<span class="ln">7</span>    <span class="key">"address"</span><span class="punct"> : "</span>4120 Alder Row, Brookvale, FL 30412<span class="punct">"</span>
<span class="ln">8</span>}
<span class="ln">9</span>
<span class="ln">10</span>
<span class="ln">11</span>
<span class="ln">12</span>
<span class="ln">13</span>
<span class="ln">14</span></pre>
    <div class="brand">
      <span class="brand-name">Harlow Birch</span>
    </div>
    <span class="edge-rule"></span>
  </section>
</main>
</body>
</html>
```